Real Estate Agency Facebook Cover Photo

We need a Facebook cover photo created for our Real Estate Business. We also need this cover photo adapted to several other platforms. Please read this google doc for full specifications of the job https://papers.vellomarsh.com/sheet/d/8QwPzLk3RtYvB2nHs7JxVaM5_cEdGoUfNpLkZrWbYq/view?mode=shared

Please also carefully read the Must Haves/Should Not Haves

Please contact me if you have any queries. Looking forward to seeing your designs!

Doran

Industry/Entity Type

Real Estate Agent

Requirements
Must have
• The Taglines 'More Money In Your Pocket' and sub tagline 'With Our Low Flat Fee To Sell Your Home'

It can then also have other elements e.g our logo, contact details and anything else you think will work well.

It must also have great graphic design work which looks custom and very clean/modern
Should not have
• Must not have poor quality stock images or anything tacky regarding money etc

```html
<!DOCTYPE html>
<html lang="en">
<head>
<meta charset="utf-8">
<title>TALVRIN – Cover Presentation</title>
<link href="https://fonts.googleapis.com/css2?family=Fira+Sans:wght@400;500;600;700&family=Josefin+Sans:wght@400;600&display=swap" rel="stylesheet">
<style>
  :root {
    --board: #6f6f6f;
    --ink-dark: #0b0b0b;
    --panel-dark: #141414;
    --footer: #1c1c1c;
    --brand-red: #f0141e;
    --deep-red: #c8001a;
    --white: #ffffff;
    --rule: #9a9a9a;
  }
  * { box-sizing: border-box; margin: 0; padding: 0; }
  html, body { width: 1200px; height: 1000px; overflow: hidden; }
  body {
    position: relative;
    background: var(--board);
    font-family: "Josefin Sans", sans-serif;
    color: var(--white);
  }
  .abs { position: absolute; }

  .profile-badge {
    left: 70px; top: 70px; width: 210px; height: 210px;
    border-radius: 50%;
    background: radial-gradient(circle at 40% 35%, #3a3a3a, #111 70%);
    display: flex; align-items: center; justify-content: center;
  }
  .brand-name {
    font-family: "Fira Sans", sans-serif;
    font-weight: 700;
    color: var(--brand-red);
    letter-spacing: 2px;
    line-height: 1;
    white-space: nowrap;
  }
  .profile-badge .brand-name { font-size: 38px; }

  .cover {
    overflow: hidden;
    background: radial-gradient(ellipse at 40% 40%, #2a2a2a, var(--ink-dark) 75%);
  }
  .cover-main { left: 312px; top: 46px; width: 855px; height: 324px; }
  .cover-alt {
    left: 613px; top: 625px; width: 559px; height: 220px;
    background: radial-gradient(ellipse at 50% 50%, #262626, var(--panel-dark) 80%);
  }
  .cover svg.chevrons { position: absolute; left: 0; top: 0; }

  .cover-main .brand-name { position: absolute; right: 100px; top: 28px; font-size: 36px; }
  .headline {
    font-family: "Fira Sans", sans-serif; font-weight: 700;
    text-align: center; white-space: nowrap; line-height: 1;
  }
  .subline {
    font-family: "Fira Sans", sans-serif; font-weight: 600;
    text-align: center; white-space: nowrap; line-height: 1;
  }
  .cover-main .headline { position: absolute; left: 0; width: 860px; top: 80px; font-size: 45px; }
  .cover-main .subline { position: absolute; left: 0; width: 860px; top: 127px; font-size: 23.5px; }

  .feature {
    position: absolute; top: 171px; width: 170px; margin-left: -85px;
    display: flex; flex-direction: column; align-items: center;
  }
  .feature-icon {
    width: 64px; height: 64px; border-radius: 50%;
    background: var(--brand-red);
    box-shadow: 0 0 10px rgba(240,20,30,.6);
    border: 3px solid #ff4d55;
    display: flex; align-items: center; justify-content: center;
  }
  .feature-icon.is-light { background: var(--white); border-color: var(--white); }
  .feature-label {
    margin-top: 4px; font-family: "Fira Sans", sans-serif; font-weight: 600;
    font-size: 13px; white-space: nowrap;
  }
  .contact-rule { position: absolute; left: 30px; right: 30px; top: 265px; height: 3px; background: linear-gradient(90deg, transparent, var(--rule), transparent); }
  .contact-row {
    position: absolute; top: 278px; left: 40px; width: 776px;
    display: flex; justify-content: space-between; align-items: center;
    font-family: "Fira Sans", sans-serif; font-weight: 500; font-size: 16.5px;
  }
  .contact-item { display: flex; align-items: center; gap: 10px; white-space: nowrap; }

  .cover-alt .brand-name { position: absolute; left: 0; width: 559px; text-align: center; top: 66px; font-size: 56px; }
  .cover-alt .headline { position: absolute; left: 0; width: 559px; top: 129px; font-size: 25px; }
  .cover-alt .subline { position: absolute; left: 0; width: 559px; top: 156px; font-size: 13px; }

  .wordmark-study { left: 96px; top: 494px; }
  .wordmark-study .brand-name { font-size: 52px; }
  .symbol-study { left: 478px; top: 470px; width: 145px; text-align: center; }
  .symbol-study .brand-name { font-size: 24px; }
  .pattern-field {
    left: 22px; top: 620px; width: 501px; height: 223px;
    background: linear-gradient(135deg, #d42a30, #b52228);
    opacity: .85;
  }
  .rationale {
    left: 610px; top: 432px; width: 590px;
    text-align: center; font-weight: 400; font-size: 18px; line-height: 25px;
  }
  .footer-band {
    left: 0; top: 886px; width: 1200px; height: 114px;
    background: var(--footer);
    display: flex; align-items: center; justify-content: center;
  }
  .footer-band p {
    width: 870px; text-align: center; font-family: "Fira Sans", sans-serif;
    font-weight: 400; font-size: 17.5px; line-height: 25px;
  }
  .flow-arrows { left: 0; top: 0; pointer-events: none; }
</style>
</head>
<body>

  <div class="abs profile-badge"><span class="brand-name">TALVRIN</span></div>

  <section class="abs cover cover-main">
    <svg class="chevrons" width="855" height="324" viewBox="0 0 855 324">
      <polygon points="0,0 45,0 103,164 45,324 0,324 60,164" fill="var(--deep-red)"/>
      <polygon points="60,164 103,164 45,324 0,324" fill="var(--brand-red)"/>
      <polygon points="855,0 810,0 751,164 810,324 855,324 796,164" fill="var(--deep-red)"/>
      <polygon points="796,164 751,164 810,324 855,324" fill="var(--brand-red)"/>
    </svg>
    <span class="brand-name">TALVRIN</span>
    <h1 class="headline">More Money In Your Pocket</h1>
    <p class="subline">With Our Low Flat Fee To Sell Your Home</p>

    <div class="feature" style="left:243px">
      <div class="feature-icon">
        <svg width="36" height="36" viewBox="0 0 36 36"><g stroke="#fff" stroke-width="3" fill="none"><line x1="8" y1="28" x2="28" y2="8"/><circle cx="10" cy="10" r="4"/><circle cx="26" cy="26" r="4"/></g></svg>
      </div>
      <span class="feature-label">NO COMMISSION</span>
    </div>
    <div class="feature" style="left:427px">
      <div class="feature-icon is-light">
        <svg width="36" height="36" viewBox="0 0 36 36"><g stroke="var(--brand-red)" stroke-width="3" fill="none"><circle cx="18" cy="11" r="7"/><path d="M18 20 V32 M12 26 L18 32 L24 26"/></g></svg>
      </div>
      <span class="feature-label">LOW FLAT FEE</span>
    </div>
    <div class="feature" style="left:610px">
      <div class="feature-icon">
        <svg width="36" height="36" viewBox="0 0 36 36"><g stroke="#fff" stroke-width="2.5" fill="none"><circle cx="18" cy="18" r="14"/><circle cx="18" cy="18" r="9"/></g><text x="18" y="23" font-size="13" font-family="Fira Sans, sans-serif" font-weight="700" fill="#fff" text-anchor="middle">$</text></svg>
      </div>
      <span class="feature-label">BEST SELLING PRICE</span>
    </div>

    <div class="contact-rule"></div>
    <div class="contact-row">
      <span class="contact-item">
        <svg width="32" height="22" viewBox="0 0 32 22"><path d="M2 4 H8 M0 10 H8 M2 16 H8" stroke="var(--brand-red)" stroke-width="2"/><rect x="10" y="2" width="22" height="16" fill="var(--brand-red)"/><path d="M10 2 L21 11 L32 2" stroke="#000" stroke-width="1.5" fill="none"/></svg>
        48 Harlow Street Brenton NSW 2190
      </span>
      <span class="contact-item">
        <svg width="24" height="24" viewBox="0 0 24 24"><path d="M5 2 L9 2 L10 7 L7 9 C8 12 11 15 14 16 L16 13 L21 14 L21 19 C21 21 19 22 17 22 C9 21 3 15 2 7 C2 4 3 2 5 2 Z" fill="var(--brand-red)"/></svg>
        +61 2 5550 1942
      </span>
      <span class="contact-item">
        <svg width="28" height="20" viewBox="0 0 28 20"><rect x="0" y="0" width="28" height="20" fill="var(--brand-red)"/><path d="M0 0 L14 11 L28 0" stroke="#000" stroke-width="1.5" fill="none"/></svg>
        info@talvrin-homes.example
      </span>
    </div>
  </section>

  <div class="abs wordmark-study"><span class="brand-name">TALVRIN</span></div>
  <div class="abs symbol-study"><span class="brand-name">TALVRIN</span></div>

  <div class="abs pattern-field" role="img" aria-label="Repeating red lattice pattern built from the brand symbol"></div>

  <p class="abs rationale">this is the justification that I am using&nbsp; your brand<br>to the maximum in order to impose it in the development of<br>your corporate image for multiple uses,&nbsp; to which they apply,<br>hence the reason why they peared on the banner and<br>at the same time gives it some strength with the red of<br>your color palette.</p>

  <section class="abs cover cover-alt" role="group" aria-label="Alternate cover with subtle lattice background">
    <svg class="chevrons" width="559" height="220" viewBox="0 0 559 220">
      <polygon points="0,0 30,0 95,110 30,220 0,220 55,110" fill="var(--deep-red)"/>
      <polygon points="55,110 95,110 30,220 0,220" fill="var(--brand-red)"/>
      <polygon points="559,0 529,0 466,110 529,220 559,220 505,110" fill="var(--deep-red)"/>
      <polygon points="505,110 466,110 529,220 559,220" fill="var(--brand-red)"/>
    </svg>
    <span class="brand-name">TALVRIN</span>
    <h2 class="headline">More Money In Your Pocket</h2>
    <p class="subline">With Our Low Flat Fee To Sell Your Home</p>
  </section>

  <svg class="abs flow-arrows" width="1200" height="1000" viewBox="0 0 1200 1000">
    <defs>
      <marker id="head" markerWidth="8" markerHeight="8" refX="7" refY="4" orient="auto">
        <path d="M0 0 L8 4 L0 8 Z" fill="#111"/>
      </marker>
    </defs>
    <g stroke="#111" stroke-width="1.3" fill="none" marker-end="url(#head)">
      <line x1="223" y1="464" x2="485" y2="464"/>
      <line x1="503" y1="452" x2="333" y2="377"/>
      <line x1="596" y1="556" x2="620" y2="610"/>
      <line x1="202" y1="530" x2="214" y2="606"/>
      <line x1="538" y1="734" x2="598" y2="734"/>
    </g>
  </svg>

  <footer class="abs footer-band">
    <p>Lorem ipsum dolor sit amet, consectetuer adipiscing elit, sed diam nonummy nibh euismod tincidunt<br>ut laoreet dolore magna aliquam erat volutpat. Ut wisi enim ad minim veniam, quis nostrud exerci<br>tation ullamcorper suscipit lobortis nisl ut aliquip ex ea commodo consequat.</p>
  </footer>

</body>
</html>
```